Denver-based business coaching & networking business needs marketing postcard design

We need help designing an oversized postcard that our sales team can use as a leave-behind when they are talking to different businesses and professionals. We have a program that has business owners and sales professionals attend a one day seminar to develop an executable business plan online that is ready to be implemented. Following the seminar they participate in bi-weekly group meetings where they collaborate with other professionals, review and stay accountable to their plan, and pass referrals. We would like to have a few graphics included from our website (www.trelvany.com) including the Map-Build-Connect graphic and the "Six Traps That Sink Strategies" graphic. The final design should be able to have a clear call-to-action about attending a seminar to begin their journey with Trelvany.

Language we would like to have included is as follows:

Learn Business Strategy
Create an Executable Business Plan
Receive Consistent Coaching
Attend Additional Educational Sessions
Profit from Peer Collaboration
Stay Accountable through Bi-Weekly Meetings
Increase your income through Referrals

The role of Trelvany is to develop successful business people through education, collaboration and community. This is created by first attending a one day seminar whose purpose is to assist attendees in creating an immediately executable business plan. Attendees then meet bi-weekly to pass referrals, collaborate on challenges and continually check in on their own plans, to ensure their continued success.

Target Market(s)

Age 28-45, Realtors, Mortgage Brokers, Insurance Professionals, Financial Advisors, CPA's, Attorneys, Small Business Owners

Industry/Entity Type

Business Consultant

Font styles to use
Sans Serif

Colors
faa54b
f37122

Requirements
Must have
• Trelvany logo, text that was provided in description, graphics that hit on elements from our website, call to action, website address

```html
<!DOCTYPE html>
<html lang="en">
<head>
<meta charset="utf-8">
<title>Trelvany Postcard – Front and Back</title>
<link href="https://fonts.googleapis.com/css2?family=Montserrat:wght@400;500;600;700;800&display=swap" rel="stylesheet">
<style>
  :root{
    --orange:#f37122;
    --orange-light:#faa54b;
    --charcoal:#58595b;
    --charcoal-dark:#4a4b4d;
    --ink:#2b2b2b;
    --paper:#ffffff;
    --paper-shade:#f1f1f1;
    --stage:#5b5b5b;
  }
  *{box-sizing:border-box;margin:0;padding:0}
  html,body{width:826px;height:1200px;overflow:hidden;background:var(--stage)}
  body{font-family:'Montserrat',Arial,sans-serif}
  .stage{position:absolute;left:0;top:0;width:900px;height:1308px;transform:scale(0.91778);transform-origin:0 0}
  .card{position:absolute;left:60px;width:785px;height:505px;background:var(--paper);overflow:hidden;box-shadow:4px 5px 8px rgba(0,0,0,.45)}
  .card--front{top:93px;background:linear-gradient(135deg,#fafafa,#ececec 60%,#f7f7f7)}
  .card--back{top:688px;background:linear-gradient(120deg,#f4f4f4,#fbfbfb 30%,#ededed 55%,#fafafa)}
  .card-art{position:absolute;inset:0;width:100%;height:100%}

  /* front */
  .brand-mark{position:absolute;left:80px;top:20px;width:60px;height:60px;background:var(--orange-light)}
  .brand-name{position:absolute;left:78px;top:89px;font-size:15px;font-weight:500;color:var(--charcoal);letter-spacing:.5px}
  .benefit{position:absolute;height:60px;background:var(--charcoal);border-radius:7px;color:#fff;font-weight:600;font-size:9.8px;line-height:10px;text-align:center;padding-top:24px}
  .benefit-icon{position:absolute;left:50%;top:-33px;width:50px;height:50px;margin-left:-25px;border-radius:50%;background:var(--orange);border:2px solid #fff}
  .benefit-icon::after{content:"";position:absolute;left:14px;top:14px;width:18px;height:18px;border:2px solid var(--ink);border-radius:3px}
  .web-strip{position:absolute;left:0;bottom:0;width:360px;height:35px;background:var(--orange);clip-path:polygon(0 0,100% 0,calc(100% - 34px) 100%,0 100%);display:flex;align-items:center;padding-left:96px;font-size:13px;font-weight:600;color:var(--ink)}
  .web-strip b{font-weight:800}
  .globe{position:absolute;left:68px;top:9px;width:17px;height:17px}

  /* back */
  .logo-row{position:absolute;left:30px;top:35px;display:flex;align-items:center;gap:10px}
  .logo-square{width:58px;height:56px;background:var(--orange-light)}
  .logo-name{font-size:50px;font-weight:500;color:var(--charcoal);letter-spacing:1px;line-height:1}
  .about{position:absolute;left:30px;top:128px;width:372px;font-size:12.4px;line-height:17.8px;font-weight:500;color:var(--ink);text-align:justify}
  .cta{position:absolute;left:28px;width:312px;height:35px;background:var(--orange);clip-path:polygon(0 0,100% 0,calc(100% - 12px) 100%,0 100%);display:flex;align-items:center;color:#fff;box-shadow:0 3px 4px rgba(0,0,0,.3)}
  .cta--ask{top:300px;color:var(--ink);font-weight:700;font-size:16.5px;padding-left:28px}
  .cta--phone{top:347px;font-size:24px;font-weight:700;padding-left:66px}
  .cta--web{top:392px;font-size:15px;font-weight:500;padding-left:72px}
  .cta--web b{font-weight:700}
  .cta--social{top:440px;padding-left:0}
  .cta-icon{position:absolute;left:0;top:0;width:46px;height:35px;background:var(--orange-light);border-radius:0 18px 18px 0;display:flex;align-items:center;justify-content:center}
  .follow-pill{height:35px;width:108px;background:var(--orange-light);border-radius:0 18px 18px 0;display:flex;align-items:center;padding-left:16px;color:var(--ink);font-weight:600;font-size:15px;border-right:2px solid #fff}
  .social-dots{display:flex;gap:24px;margin-left:30px}
  .social-dot{width:16px;height:16px;border-radius:50%;background:#fff}
</style>
</head>
<body>
<main class="stage">

  <section class="card card--front" aria-label="Postcard front">
    <svg class="card-art" viewBox="0 0 785 505" preserveAspectRatio="none">
      <defs>
        <linearGradient id="meeting-tones" x1="0" y1="0" x2="1" y2="1">
          <stop offset="0" stop-color="#e9e3da"/>
          <stop offset=".45" stop-color="#b49a80"/>
          <stop offset="1" stop-color="#3c4048"/>
        </linearGradient>
      </defs>
      <polygon points="130,140 300,60 330,35 225,120" fill="var(--charcoal)"/>
      <polygon points="180,130 320,70 300,100" fill="#8a8b8d"/>
      <polygon points="350,0 785,0 785,505 330,505 465,345" fill="url(#meeting-tones)" role="img" aria-label="Photo of a smiling presenter leading a business meeting around a table with laptops"/>
      <polygon points="292,0 350,0 465,345 448,345" fill="var(--orange)"/>
      <polygon points="308,505 330,505 465,345 452,345" fill="var(--charcoal)"/>
    </svg>

    <div class="brand-mark"></div>
    <div class="brand-name">TRELVANY</div>

    <div class="benefit" style="left:33px;top:185px;width:97px"><span class="benefit-icon"></span>Learn<br>Business<br>Strategy</div>
    <div class="benefit" style="left:141px;top:185px;width:97px"><span class="benefit-icon"></span>Create an<br>Executable<br>Business Plan</div>
    <div class="benefit" style="left:250px;top:185px;width:97px"><span class="benefit-icon"></span>Receive<br>Consistent<br>Coaching</div>
    <div class="benefit" style="left:61px;top:289px;width:118px"><span class="benefit-icon"></span>Attend Additional<br>Educational<br>Sessions</div>
    <div class="benefit" style="left:201px;top:289px;width:118px"><span class="benefit-icon"></span>Profit from<br>Peer<br>Collaboration</div>
    <div class="benefit" style="left:61px;top:393px;width:118px"><span class="benefit-icon"></span>Stay Accountable<br>through Bi-<br>Weekly Meetings</div>
    <div class="benefit" style="left:201px;top:393px;width:118px"><span class="benefit-icon"></span>Increase your<br>income through<br>Referrals</div>

    <div class="web-strip">
      <svg class="globe" viewBox="0 0 20 20"><circle cx="10" cy="10" r="9" fill="var(--ink)"/><g fill="none" stroke="var(--orange-light)" stroke-width="1.2"><ellipse cx="10" cy="10" rx="4" ry="8"/><line x1="2" y1="10" x2="18" y2="10"/><line x1="10" y1="2" x2="10" y2="18"/></g></svg>
      <span>www.<b>trelvany</b>.com</span>
    </div>
  </section>

  <section class="card card--back" aria-label="Postcard back">
    <svg class="card-art" viewBox="0 0 785 505" preserveAspectRatio="none">
      <polygon points="545,0 785,0 785,505 380,505" fill="#fff"/>
      <polygon points="508,0 528,0 432,290 413,290" fill="var(--charcoal)"/>
      <polygon points="528,0 546,0 382,505 342,505" fill="var(--orange)"/>
    </svg>

    <div class="logo-row">
      <span class="logo-square"></span>
      <span class="logo-name">TRELVANY</span>
    </div>

    <p class="about">The role of Trelvany is to develop successful business people through education, collaboration and community. This is created by first attending a one day seminar whose purpose is to assist attendees in creating an immediately executable business plan. Attendees then meet bi-weekly to pass referrals, collaborate on challenges and continually check in on their own plans, to ensure their continued success.</p>

    <div class="cta cta--ask">Want to find out more?</div>
    <div class="cta cta--phone">
      <span class="cta-icon"><svg width="24" height="24" viewBox="0 0 24 24"><circle cx="12" cy="12" r="11" fill="none" stroke="var(--ink)" stroke-width="1.6"/><path d="M8 6.5l2 2.5-1.2 1.5c.8 1.7 2 2.9 3.7 3.7l1.5-1.2 2.5 2-1.3 1.8c-3.8-.4-7.5-4.1-7.9-7.9z" fill="var(--ink)"/></svg></span>
      099 5521 874
    </div>
    <div class="cta cta--web">
      <span class="cta-icon"><svg width="24" height="24" viewBox="0 0 20 20"><g fill="none" stroke="var(--ink)" stroke-width="1.3"><circle cx="10" cy="10" r="8.5"/><ellipse cx="10" cy="10" rx="4" ry="8.5"/><line x1="1.5" y1="10" x2="18.5" y2="10"/><line x1="3" y1="5.5" x2="17" y2="5.5"/><line x1="3" y1="14.5" x2="17" y2="14.5"/></g></svg></span>
      <span>www.<b>trelvany</b>.com</span>
    </div>
    <div class="cta cta--social">
      <span class="follow-pill">Follow us</span>
      <span class="social-dots"><span class="social-dot"></span><span class="social-dot"></span><span class="social-dot"></span><span class="social-dot"></span></span>
    </div>
  </section>

</main>
</body>
</html>
```